Business Card Design Project

I need a business card design for our new logo, please check the logo at the following link:
https://www.filecrate.net/s/q7rtx2pw9kd41m/FernLoop.png
The address on the business card:
Av. Gervásio Tavares 418 sala 207
Barra da Tijuca, Rio de Janeiro, RJ
CEP: 22714-380
Brasil
Phone: +55 21 86347215
e-mail: osvaldo@fernloop.com.br
Updates
Thank you all for sending your designs, we will not provide feedback because there are too many designs, on December 3 we will pick the best design according to our point of view. Please keep posting.
Osvaldo
Industry/Entity Type
Business
Look and feel
Each slider illustrates characteristics of the customer's brand and the style your logo design should communicate.

```html
<!DOCTYPE html>
<html lang="pt-BR">
<head>
<meta charset="utf-8">
<title>FernLoop – Business Card</title>
<link rel="stylesheet" href="https://fonts.googleapis.com/css2?family=Pompiere&display=swap">
<style>
  :root {
    --card-bg: #ffffff;
    --ink: #1d1d1b;
    --ink-soft: #2b2b2b;
    --accent-yellow: #f5c400;
    --accent-amber: #e7a800;
    --art-grey: #b9b9b9;
    --art-dark: #3a3a3a;
  }
  * { margin: 0; padding: 0; box-sizing: border-box; }
  html, body {
    width: 1200px;
    height: 753px;
    overflow: hidden;
    background: var(--card-bg);
  }
  .card {
    position: relative;
    width: 1200px;
    height: 753px;
    background: var(--card-bg);
    font-family: "Pompiere", "Arial Narrow", sans-serif;
    color: var(--ink);
    overflow: hidden;
  }
  .brand {
    position: absolute;
    left: 84px;
    top: 318px;
    display: flex;
    align-items: center;
    gap: 18px;
  }
  .brand-dot {
    width: 34px;
    height: 34px;
    border-radius: 50%;
    background: var(--accent-yellow);
  }
  .brand-name {
    font-size: 92px;
    line-height: 1;
    color: var(--ink);
    font-weight: 400;
  }
  .contact {
    position: absolute;
    left: 600px;
    top: 94px;
    font-size: 32px;
    line-height: 50px;
    color: var(--ink-soft);
    font-style: normal;
  }
  .contact .gap { height: 50px; }
  .artwork {
    position: absolute;
    right: 0;
    bottom: 0;
    width: 620px;
    height: 440px;
    background:
      radial-gradient(ellipse 38% 42% at 62% 66%, var(--accent-yellow) 0%, var(--accent-amber) 45%, rgba(231,168,0,0) 80%),
      radial-gradient(ellipse 55% 60% at 60% 70%, var(--art-dark) 0%, rgba(58,58,58,0.55) 45%, rgba(58,58,58,0) 85%),
      radial-gradient(ellipse 70% 75% at 70% 60%, rgba(185,185,185,0.6) 0%, rgba(185,185,185,0) 80%);
  }
</style>
</head>
<body>
  <main class="card">
    <div class="brand">
      <span class="brand-dot"></span>
      <span class="brand-name">FernLoop</span>
    </div>

    <address class="contact">
      <div>Av. Gervásio Tavares 418 sala 207</div>
      <div>Barra da Tijuca, Rio de Janeiro, RJ</div>
      <div>CEP: 22714-380</div>
      <div>Brasil</div>
      <div class="gap"></div>
      <div>Phone: +55 21 86347215</div>
      <div>Email: osvaldo@fernloop.com.br</div>
    </address>

    <div class="artwork" role="img" aria-label="Graffiti-style 3D lettering illustration in yellow, black and grey with spray splatter"></div>
  </main>
</body>
</html>
```